We need a MODERN credit application banner

We have a program that helps people get pre-qualified for an auto loan. Our current Application page/Success page is dated and does not have the colors we want. I want to use fonts and colors that match our partner CrestLedger (www.crestledger.example). I want to include their powered by logo, tallyrank logo, and swift4lending logo all in a matching CrestLedger Color scheme. I also need a Favicon that matches your design for the page. I attached our deck so you can get more content. To be clear the application page and success pages below are the targets of this redesign! You can visit www.pbelmorepromo.example to get more information from our website or www.swift4lending.example.

Target Market(s)

Car dealers and their consumers

Industry/Entity Type

Automotive

Requirements
Must have
• It must offer the same data that is on the existing art
Nice to have
• Looking for a Clean but Interesting design.
Should not have
• No red and black. Do not change the form fills.

```html
<!DOCTYPE html>
<html lang="en">
<head>
<meta charset="utf-8">
<title>Credit Pre-Qualification – Application and Success</title>
<link rel="stylesheet" href="https://fonts.googleapis.com/css2?family=Montserrat:wght@500;600;700;800&family=Nunito:ital,wght@0,400;0,600;0,700;1,400;1,800&display=swap">
<style>
  :root {
    --cyan: #00a9d1;
    --yellow: #fcd800;
    --navy: #23607f;
    --field: #e6e7e8;
    --footer: #e6e7e8;
    --ink: #1d1d1b;
    --muted: #6d6e70;
    --white: #ffffff;
  }
  * { box-sizing: border-box; margin: 0; padding: 0; }
  html, body { width: 677px; height: 1200px; overflow: hidden; background: var(--white); }
  body { position: relative; font-family: "Nunito", sans-serif; color: var(--ink); }

  .panel {
    position: absolute; left: 27px; width: 621px; background: var(--white);
    box-shadow: 0 6px 16px rgba(0,0,0,0.18); overflow: hidden;
  }
  .panel--apply { top: 27px; height: 524px; }
  .panel--success { top: 601px; height: 562px; }
  .abs { position: absolute; }

  /* header */
  .apply-header { left: 0; top: 0; width: 100%; height: 91px; background: var(--cyan); border-bottom: 3px solid var(--yellow); }
  .apply-title { left: 92px; top: 20px; font-family: "Montserrat", sans-serif; font-weight: 800; font-size: 27px; color: var(--white); letter-spacing: 0.2px; }
  .apply-subtitle { left: 92px; top: 51px; font-family: "Montserrat", sans-serif; font-weight: 600; font-size: 17.5px; color: var(--yellow); }

  /* form */
  .field { height: 17px; width: 147px; background: var(--field); font-size: 7.2px; color: var(--muted); padding-left: 12px; line-height: 17px; }
  .col-a { left: 92px; } .col-b { left: 257px; }
  .field--select::after {
    content: ""; position: absolute; right: 10px; top: 4px; width: 5px; height: 5px;
    border-right: 1px solid var(--muted); border-bottom: 1px solid var(--muted); transform: rotate(45deg);
  }
  .dob-label { width: 54px; }
  .dob-part { height: 17px; width: 29px; background: #d9dadb; top: 249px; }
  .dob-part::after {
    content: ""; position: absolute; right: 8px; top: 4px; width: 5px; height: 5px;
    border-right: 1px solid var(--muted); border-bottom: 1px solid var(--muted); transform: rotate(45deg);
  }
  .verify-note { left: 92px; top: 303px; height: 8.5px; width: 113px; background: var(--cyan); color: var(--white); font-size: 5.2px; font-weight: 700; line-height: 8.5px; padding-left: 5px; }
  .vehicle-label { left: 92px; top: 327px; font-size: 7.4px; color: var(--muted); }
  .btn {
    display: flex; align-items: center; justify-content: center; background: var(--yellow);
    border-radius: 20px; font-family: "Montserrat", sans-serif; font-weight: 800; color: var(--ink);
  }
  .btn--result { left: 92px; top: 377px; width: 88px; height: 27px; font-size: 8.4px; }

  /* benefits */
  .benefits { left: 417px; top: 143px; width: 107px; height: 263px; background: var(--navy); color: var(--white); text-align: center; font-family: "Montserrat", sans-serif; font-weight: 500; }
  .benefits__title { position: absolute; top: 13px; width: 100%; font-size: 9.6px; line-height: 12.5px; }
  .benefits__powered { position: absolute; top: 44px; left: 17px; font-size: 4.5px; text-align: left; }
  .benefits__brand { position: absolute; top: 50px; width: 100%; font-size: 11px; font-weight: 600; }
  .benefit-icon { position: absolute; left: 38px; }
  .benefit-text { position: absolute; width: 100%; font-size: 9.6px; line-height: 12.5px; }

  /* footer */
  .footer { left: 0; width: 100%; height: 65px; background: var(--footer); }
  .footer__lead { left: 110px; top: 26px; font-size: 10px; font-weight: 700; color: var(--navy); }
  .footer__brand { top: 22px; font-family: "Nunito", sans-serif; font-weight: 600; font-size: 14.5px; color: var(--navy); }
  .footer__mark { top: 26px; width: 15px; height: 15px; background: var(--navy); }
  .footer__divider { top: 19px; width: 1px; height: 28px; background: var(--navy); }

  /* success */
  .success-title { left: 92px; top: 18px; font-family: "Montserrat", sans-serif; font-weight: 800; font-size: 27px; color: var(--cyan); }
  .success-subtitle { left: 92px; top: 50px; font-family: "Montserrat", sans-serif; font-weight: 600; font-size: 16.5px; color: var(--navy); }
  .success-band { left: 0; top: 91px; width: 100%; height: 181px; background: var(--navy); border-top: 4px solid var(--yellow); }
  .congrats { left: 95px; top: 134px; font-family: "Montserrat", sans-serif; font-weight: 800; font-size: 26px; color: var(--yellow); letter-spacing: 0.2px; }
  .congrats-amount { left: 95px; top: 165px; font-family: "Montserrat", sans-serif; font-weight: 500; font-size: 17.5px; color: var(--white); }
  .btn--contact { left: 95px; top: 212px; width: 266px; height: 26px; font-size: 9.4px; }

  .phone { left: 400px; top: 113px; width: 104px; height: 213px; background: var(--white); border: 4px solid #222; border-radius: 16px; }
  .phone__notch { left: 30px; top: -1px; width: 36px; height: 8px; background: #222; border-radius: 0 0 6px 6px; }
  .phone__label { width: 100%; text-align: center; font-family: "Montserrat", sans-serif; font-weight: 600; font-size: 7.6px; color: var(--ink); line-height: 10px; left: 0; }
  .donut { left: 6px; top: 61px; }
  .donut__value { left: 0; top: 87px; width: 100%; text-align: center; font-family: "Montserrat", sans-serif; font-weight: 500; font-size: 25px; color: #4a4a4a; }

  .next-title { left: 97px; top: 288px; font-family: "Montserrat", sans-serif; font-weight: 700; font-size: 15px; color: var(--ink); }
  .next-steps { left: 98px; top: 314px; font-size: 8.2px; font-style: italic; line-height: 10.6px; color: var(--ink); list-style: none; }
  .next-steps a { color: var(--cyan); font-weight: 800; text-decoration: none; }
  .btn--small { top: 363px; width: 108px; height: 19px; font-size: 7.4px; }
  .valid-note { left: 98px; top: 397px; font-size: 7.8px; color: var(--ink); }
  .act-now { left: 97px; top: 408px; font-family: "Montserrat", sans-serif; font-weight: 700; font-size: 15px; color: var(--navy); }

  .gauge { left: 387px; top: 340px; }
  .gauge__value { left: 432px; top: 396px; width: 42px; text-align: center; font-family: "Montserrat", sans-serif; font-weight: 700; font-size: 11px; color: var(--white); }
  .score-label { left: 387px; top: 418px; width: 132px; text-align: center; font-family: "Montserrat", sans-serif; font-weight: 700; font-size: 13px; color: var(--ink); }
  .score-rule { left: 387px; width: 132px; height: 2.5px; background: var(--field); }
</style>
</head>
<body>

<section class="panel panel--apply" aria-label="Credit application">
  <header class="abs apply-header"></header>
  <h1 class="abs apply-title">Get your free Credit Score</h1>
  <p class="abs apply-subtitle">and get pre-qualified instantly</p>

  <div class="abs field col-a" style="top:144px">First Name</div>
  <div class="abs field col-b" style="top:144px">Last Name</div>
  <div class="abs field col-a" style="top:179px">Address</div>
  <div class="abs field col-b" style="top:179px">Apartment</div>
  <div class="abs field col-a" style="top:214px">City</div>
  <div class="abs field col-b" style="top:214px">State</div>
  <div class="abs field col-a" style="top:249px">Zip</div>
  <div class="abs field col-b dob-label" style="top:249px">Date of Birt</div>
  <div class="abs dob-part" style="left:311px"></div>
  <div class="abs dob-part" style="left:342px"></div>
  <div class="abs dob-part" style="left:374px"></div>
  <div class="abs field col-a" style="top:284px">Mobile Phone</div>
  <div class="abs field col-b" style="top:284px">Email</div>
  <div class="abs verify-note">correct number needed for verification</div>

  <p class="abs vehicle-label">The vehicle I’m most interested in is:</p>
  <div class="abs field field--select col-a" style="top:341px">Category</div>
  <div class="abs field field--select col-b" style="top:341px">Make</div>

  <div class="abs btn btn--result">GET RESULT</div>

  <aside class="abs benefits">
    <p class="benefits__title">Free<br>Credit Score</p>
    <p class="benefits__powered">powered by:</p>
    <p class="benefits__brand">CrestLedger</p>
    <svg class="benefit-icon" style="top:90px" width="30" height="30" viewBox="0 0 30 30" aria-hidden="true">
      <path d="M3 2h22a2 2 0 0 1 2 2v12a2 2 0 0 1-2 2H12l-6 6v-6H3a2 2 0 0 1-2-2V4a2 2 0 0 1 2-2z" fill="#fff"/>
      <circle cx="24" cy="18" r="5" fill="#fff" stroke="#23607f" stroke-width="1.5"/>
      <path d="M22 16l4 4M26 16l-4 4" stroke="#23607f" stroke-width="1.4"/>
    </svg>
    <p class="benefit-text" style="top:125px">No social security<br>number required</p>
    <svg class="benefit-icon" style="top:177px" width="32" height="30" viewBox="0 0 32 30" aria-hidden="true">
      <rect x="1" y="2" width="26" height="19" rx="2.5" fill="#fff"/>
      <rect x="1" y="8" width="26" height="3.5" fill="#23607f"/>
      <rect x="4" y="15" width="7" height="2" fill="#23607f"/>
      <circle cx="24" cy="21" r="6" fill="#fff" stroke="#23607f" stroke-width="1.5"/>
      <path d="M21 21l2.2 2.2 4-4" stroke="#23607f" stroke-width="1.6" fill="none"/>
    </svg>
    <p class="benefit-text" style="top:213px">No impact on your<br>credit score</p>
  </aside>

  <footer class="abs footer" style="top:459px">
    <span class="abs footer__lead">powered by:</span>
    <span class="abs footer__mark" style="left:190px"></span>
    <span class="abs footer__brand" style="left:210px">tallyrank</span>
    <span class="abs footer__divider" style="left:309px"></span>
    <span class="abs footer__brand" style="left:320px">swift4lending</span>
    <span class="abs footer__divider" style="left:412px"></span>
    <span class="abs footer__brand" style="left:420px">CrestLedger</span>
  </footer>
</section>

<section class="panel panel--success" aria-label="Pre-qualification result">
  <h2 class="abs success-title">Success</h2>
  <p class="abs success-subtitle">view your credit score and pre-qualification amount</p>

  <div class="abs success-band"></div>
  <p class="abs congrats">CONGRATULATIONS!</p>
  <p class="abs congrats-amount">YOU PRE-QUALIFY UP TO $75, 000</p>
  <div class="abs btn btn--contact">THE DEALER WILL CONTACT YOU SHORTLY OR</div>

  <div class="abs phone">
    <span class="abs phone__notch"></span>
    <p class="abs phone__label" style="top:50px">UP TO</p>
    <svg class="abs donut" width="85" height="85" viewBox="0 0 85 85" aria-hidden="true">
      <circle cx="42.5" cy="42.5" r="38" fill="none" stroke="#e6e7e8" stroke-width="7"/>
      <circle cx="42.5" cy="42.5" r="38" fill="none" stroke="#00a9d1" stroke-width="7"
              stroke-dasharray="179.1 238.8" transform="rotate(-90 42.5 42.5)"/>
    </svg>
    <p class="abs donut__value" style="top:86px">75%</p>
    <p class="abs phone__label" style="top:151px">PRE-QUALIFIED<br>AMOUNT</p>
  </div>

  <h3 class="abs next-title">You Can Take the Next Step!</h3>
  <ol class="abs next-steps">
    <li>1. Call Northgate Auto at 555-014-2290</li>
    <li>2. Email them by <a href="#">Clicking Here</a></li>
    <li>3. Print this page and take it to Northgate Auto</li>
  </ol>
  <div class="abs btn btn--small" style="left:98px">PRINTABLE VERSION</div>
  <div class="abs btn btn--small" style="left:214px">MAP TO DEALER</div>
  <p class="abs valid-note">Your pre-qualification is valid for a limited time</p>
  <p class="abs act-now">Act Now!</p>

  <svg class="abs gauge" width="132" height="72" viewBox="0 0 132 72" aria-hidden="true">
    <path d="M1 69a65 65 0 0 1 130 0" fill="none" stroke="#e6e7e8" stroke-width="3"/>
    <path d="M14.5 69A51 51 0 0 1 23.8 39.6" fill="none" stroke="#e04a12" stroke-width="27"/>
    <path d="M23.8 39.6A51 51 0 0 1 65.5 18" fill="none" stroke="#f47a00" stroke-width="27"/>
    <path d="M65.5 18A51 51 0 0 1 96 28" fill="none" stroke="#fbc500" stroke-width="27"/>
    <path d="M96 28A51 51 0 0 1 116.5 69" fill="none" stroke="#97b004" stroke-width="27"/>
    <path d="M28 69a37.5 37.5 0 0 1 75 0z" fill="#e6e7e8"/>
    <polygon points="92,14 59,60 72,66" fill="#e8352a"/>
    <path d="M44 69a21.5 21.5 0 0 1 43 0z" fill="#333333"/>
  </svg>
  <p class="abs gauge__value">703</p>
  <p class="abs score-label">Your tallyrank</p>
  <span class="abs score-rule" style="top:447px"></span>
  <span class="abs score-rule" style="top:455px"></span>

  <footer class="abs footer" style="top:497px">
    <span class="abs footer__lead">powered by:</span>
    <span class="abs footer__mark" style="left:190px"></span>
    <span class="abs footer__brand" style="left:210px">tallyrank</span>
    <span class="abs footer__divider" style="left:309px"></span>
    <span class="abs footer__brand" style="left:320px">swift4lending</span>
    <span class="abs footer__divider" style="left:412px"></span>
    <span class="abs footer__brand" style="left:420px">CrestLedger</span>
  </footer>
</section>

</body>
</html>
```